A reimagined website for a cross-border tax firm

There are two aspects to this project for Brindlemoor Tax Advisory:
1) I need a logo update to accommodate increasing focus and specialization in my business. The byline under the name “Brindlemoor Tax Advisory” needs to change:
ORIGINAL: TAX SUPPORT FOR PUBLIC ACCOUNTING FIRMS
REVISED: CROSS-BORDER TAX SERVICES • U.S. & CANADA
2) I need a website “refresh” (see current website at www.levyhelpdesk.example) based on this logo – a new vision for a website with greater clarity, focus and organization. It should represent a re-envisioning of the current approach, and not the wholesale abandonment of the style represented there. I need it to be creative, compelling and attention grabbing, but still professional. This should, at a minimum, update any places where the old name/logo is used, but I want the redesign to go beyond this to something more intuitive. I need high quality separate PNG files of the various logo styles for use in various documents, but HTML coding would be a helpful but not necessary addition.

Target Market(s)

People in need of cross-border tax services - Canada and US

Coding

Number of Pages Required

Requirements
Must have
• Greater crispness, sharpness - higher resolution
• A more compelling, organized approach - make the wording and images more accessible to the website user (especially the staff bios, which have scroll bars now)
Nice to have
• Replacement of stock image with a true image of the Halifax skyline
Should not have
• Deviate from colour pattern represented in website logo of blue/orange
• Deviate from existing logo except for word replacement

```html
<!DOCTYPE html>
<html lang="en">
<head>
<meta charset="utf-8">
<title>Brindlemoor Tax Advisory</title>
<link href="https://fonts.googleapis.com/css2?family=Cinzel:wght@400;700&family=Open+Sans:wght@400;600;700&display=swap" rel="stylesheet">
<style>
:root{
  --navy:#1d3461;
  --navy-deep:#172a50;
  --orange:#ef6a2d;
  --blue:#2a8fd4;
  --sky:#4fa3d6;
  --grey-bg:#f3f3f3;
  --text:#444;
  --muted:#777;
  --white:#fff;
}
*{box-sizing:border-box;margin:0;padding:0}
html,body{width:1200px;height:3727px;overflow:hidden}
body{font-family:"Open Sans",Arial,sans-serif;color:var(--text);background:var(--white);position:relative}
section,header,footer{position:absolute;left:0;width:1200px}
.btn{display:inline-block;font-family:"Cinzel",Georgia,serif;font-weight:700;font-size:20px;color:var(--white);padding:14px 36px;letter-spacing:.5px}
.btn-navy{background:var(--navy)}
.btn-blue{background:var(--blue)}
.btn-outline{border:2px solid var(--white)}

/* header */
.site-header{top:0;height:130px;background:var(--white)}
.brand{position:absolute;left:75px;top:22px;width:190px;text-align:center}
.brand-square{width:40px;height:40px;background:var(--orange);margin:0 auto 6px}
.brand-name{font-family:"Cinzel",Georgia,serif;font-weight:700;font-size:13px;color:var(--navy);white-space:nowrap}
.main-nav{position:absolute;left:290px;top:56px;display:flex;gap:8px}
.main-nav a{font-family:"Cinzel",Georgia,serif;font-size:17px;color:var(--navy);padding:8px 10px;text-decoration:none}
.main-nav a.active{border:2px solid var(--orange);border-radius:4px;font-weight:700}
.header-tools{position:absolute;right:75px;top:10px;display:flex;align-items:center;gap:8px}
.social-dot{width:30px;height:30px;border-radius:50%;background:var(--navy)}
.social-dot.alt{background:#d44638}.social-dot.sky{background:var(--blue)}
.search{margin-left:18px;width:140px;border-bottom:1px solid #ccc;font-size:14px;color:#999;padding:4px 0;display:flex;justify-content:space-between}

/* hero */
.hero{top:130px;height:573px;background:linear-gradient(180deg,#c9b89a 0%,#8a8f95 45%,#3c4a5c 100%);text-align:center}
.hero h1{position:absolute;top:160px;left:0;width:100%;font-family:"Cinzel",Georgia,serif;font-size:52px;font-weight:700;color:var(--navy);line-height:1.1}
.hero .sub{position:absolute;top:300px;left:0;width:100%;font-family:"Cinzel",Georgia,serif;font-size:26px;font-weight:700;color:var(--white)}
.hero .actions{position:absolute;top:370px;left:0;width:100%;display:flex;justify-content:center;gap:10px}

/* welcome */
.welcome{top:703px;height:415px}
.welcome h2{position:absolute;left:78px;top:62px;width:560px;font-family:"Cinzel",Georgia,serif;font-size:36px;font-weight:700;color:var(--navy);line-height:1.05}
.welcome p{position:absolute;left:78px;top:148px;width:560px;font-size:13.5px;line-height:1.65}
.welcome .btn{position:absolute;left:78px;top:300px}
.video{position:absolute;left:686px;top:65px;width:438px;height:290px;background:linear-gradient(135deg,#6ea6cf,#3a7fb4)}
.video svg{position:absolute;left:179px;top:105px}

/* team */
.team{top:1118px;height:502px;background:var(--grey-bg);text-align:center}
.section-title{font-family:"Cinzel",Georgia,serif;font-weight:700;color:var(--navy);font-size:36px}
.team .section-title{margin-top:60px;display:flex;justify-content:center;align-items:center;gap:12px}
.team .lead{font-size:14px;font-style:italic;color:var(--muted);margin-top:10px}
.members{position:absolute;top:174px;left:0;width:100%}
.member{position:absolute;width:260px;height:260px;border-radius:50%;background:radial-gradient(circle at 50% 45%,#555 0%,#2a2a2a 75%)}
.member.light{background:radial-gradient(circle at 50% 45%,#e6e6e6 0%,#b9b9b9 80%)}
.member .tag{position:absolute;left:40px;top:150px;width:180px;background:var(--orange);color:var(--white);font-family:"Cinzel",Georgia,serif;font-weight:700;font-size:15px;padding:6px 4px;line-height:1.2}

/* payment */
.payment{top:1622px;height:333px;background:var(--navy)}
.payment .art{position:absolute;left:75px;top:50px;width:290px;height:230px;border-radius:6px;background:linear-gradient(160deg,#2f4f8f 0%,#253f77 55%,#6b3550 100%)}
.payment h2{position:absolute;left:388px;top:42px;font-family:"Cinzel",Georgia,serif;font-size:36px;font-weight:700;color:var(--white)}
.payment p{position:absolute;left:388px;top:100px;width:730px;font-size:14.5px;line-height:1.8;color:var(--white)}
.payment .actions{position:absolute;left:388px;top:200px;display:flex;gap:14px}

/* services */
.services{top:1955px;height:519px}
.service{position:absolute;top:62px;width:500px}
.service.ind{left:75px}.service.firms{left:616px}
.services .divider{position:absolute;left:600px;top:62px;width:1px;height:420px;background:#ddd}
.service .icon{position:absolute;left:0;top:0;width:120px;height:120px;border:5px solid var(--orange);border-radius:10px;background:var(--blue);display:flex;align-items:center;justify-content:center}
.service h3{margin-left:150px;font-family:"Cinzel",Georgia,serif;font-size:36px;font-weight:700;color:var(--navy);line-height:1.05}
.service .intro{margin-left:150px;margin-top:14px;font-size:13.5px;line-height:1.6}
.service ul{list-style:none;margin-left:150px;margin-top:18px}
.service li{font-size:19px;color:#555;margin-bottom:22px;display:flex;align-items:center;gap:14px}
.service li::before{content:"";width:16px;height:16px;border:2px solid var(--blue);border-bottom-color:var(--orange);border-left-color:var(--orange);border-radius:2px}

/* testimonial */
.testimonial{top:2474px;height:333px;background:linear-gradient(180deg,#5fb2e0,#3d8cc4 70%,#2b76b0);text-align:center;color:var(--white)}
.testimonial .section-title{margin-top:48px}
.testimonial blockquote{position:relative;width:800px;margin:26px auto 0;font-size:15.5px;line-height:1.6;text-align:center}
.testimonial .quote-mark{position:absolute;left:-70px;top:-10px}
.testimonial cite{display:block;margin-top:26px;font-style:normal;font-weight:700;font-size:16px}
.testimonial .role{font-size:12px;font-style:italic}
.dots{display:flex;justify-content:center;gap:8px;margin-top:12px}
.dots i{width:9px;height:9px;border-radius:50%;border:1px solid var(--white)}
.dots i.on{background:var(--white)}

/* blog */
.blog{top:2807px;height:447px;text-align:center}
.blog .section-title{margin-top:60px}
.posts{position:absolute;top:145px;left:75px;width:1050px;display:flex;justify-content:space-between}
.post{width:345px;text-align:left;padding:12px 0 24px 0;box-shadow:6px 6px 10px -6px rgba(0,0,0,.15)}
.post h4{font-family:"Cinzel",Georgia,serif;font-weight:700;color:var(--orange);font-size:17px}
.post .date{font-size:13px;font-style:italic;color:#555;margin-top:10px;display:flex;align-items:center;gap:8px}
.post p{font-size:13.5px;line-height:1.7;color:#666;margin-top:24px}

/* footer */
.site-footer{top:3254px;height:473px;background:#f7f7f7}
.cta{position:absolute;left:107px;top:3145px;width:986px;height:208px;background:var(--orange);text-align:center;color:var(--white);z-index:2}
.cta h2{font-family:"Cinzel",Georgia,serif;font-weight:700;font-size:30px;margin-top:44px}
.cta p{font-size:14px;font-style:italic;margin-top:4px}
.cta .btn{margin-top:24px;padding:12px 30px}
.foot-col{position:absolute;top:148px}
.foot-col h5{font-family:"Cinzel",Georgia,serif;font-weight:700;font-size:16px;color:var(--navy);margin-bottom:16px}
.foot-brand{left:75px;width:230px;text-align:center}
.foot-brand p{font-size:13.5px;line-height:1.5;margin-top:8px}
.foot-social{display:flex;justify-content:center;gap:8px;margin-top:18px}
.foot-social span{width:36px;height:36px;border-radius:50%;border:2px solid var(--orange)}
.foot-social span:first-child{background:var(--orange)}
.foot-links{left:350px}
.foot-links li{list-style:none;font-size:13.5px;line-height:1.6;display:flex;align-items:center;gap:8px}
.foot-links li::before{content:"›";color:var(--orange);font-weight:700}
.foot-contact{left:570px}
.foot-contact .row{display:flex;gap:14px;font-size:13.5px;line-height:1.5;margin-bottom:14px}
.foot-news{left:873px;width:252px}
.foot-news .hint{font-size:13px;color:#999}
.foot-news .field{margin-top:14px;height:44px;background:var(--orange);color:var(--white);font-size:13px;padding:12px}
.foot-news .subscribe{display:inline-block;margin-top:14px;background:var(--blue);color:var(--white);font-family:"Cinzel",Georgia,serif;font-weight:700;font-size:19px;padding:12px 26px;border-radius:30px}
.copyright{position:absolute;left:0;bottom:0;width:100%;height:63px;border-top:1px solid #ddd;text-align:center;line-height:63px;font-size:14px}
</style>
</head>
<body>

<header class="site-header">
  <div class="brand">
    <div class="brand-square"></div>
    <div class="brand-name">Brindlemoor Tax Advisory</div>
  </div>
  <nav class="main-nav">
    <a class="active">Home</a><a>Our Team</a><a>For Individuals</a><a>For Public Accounting Firms</a><a>Contact</a><a>Payment</a>
  </nav>
  <div class="header-tools">
    <span class="social-dot"></span><span class="social-dot alt"></span><span class="social-dot sky"></span><span class="social-dot"></span>
    <div class="search"><span>Type Here...</span>
      <svg width="14" height="14" viewBox="0 0 14 14"><circle cx="6" cy="6" r="4.5" fill="none" stroke="#333" stroke-width="2"/><line x1="9" y1="9" x2="13" y2="13" stroke="#333" stroke-width="2"/></svg>
    </div>
  </div>
</header>

<section class="hero" role="img" aria-label="City skyline at sunset seen from above">
  <h1>Tax Support for Public<br>Accounting Firms</h1>
  <div class="sub">Cross-Border Tax Services</div>
  <div class="actions"><span class="btn btn-navy">Read More</span><span class="btn btn-blue">Contact Us</span></div>
</section>

<section class="welcome">
  <h2>Wel Come to Brindlemoor Tax Advisory</h2>
  <p>Lorem Ipsum is simply dummy text of the printing and typesetting industry. Lorem Ipsum has been the industry's standard dummy text ever since the 1500s, when an unknown printer took a galley of type and scrambled it to make a type specimen book. It has survived not only five centuries.It has survived not only five centuries, but also the leap into electronic typesetting, remaining essentially unchanged.</p>
  <span class="btn btn-navy">Read More</span>
  <div class="video" role="img" aria-label="Video still of tax documents on a desk">
    <svg width="80" height="80" viewBox="0 0 80 80"><circle cx="40" cy="40" r="36" fill="none" stroke="#fff" stroke-width="4"/><path d="M32 24 L58 40 L32 56 Z" fill="#fff"/></svg>
  </div>
</section>

<section class="team">
  <h2 class="section-title">
    <svg width="38" height="32" viewBox="0 0 38 32"><circle cx="19" cy="9" r="7" fill="var(--orange)"/><circle cx="7" cy="14" r="5" fill="var(--orange)"/><circle cx="31" cy="14" r="5" fill="var(--orange)"/><path d="M8 32 Q19 14 30 32Z" fill="var(--orange)"/></svg>
    Meet Our Team
  </h2>
  <p class="lead">Corwin is chartered professional accountant (CPA) and an enrolled agent (EA).</p>
  <div class="members">
    <div class="member" style="left:104px" role="img" aria-label="Portrait of Corwin T. Hale"><div class="tag">Corwin T. Hale, CPA, CGA, EA</div></div>
    <div class="member light" style="left:469px" role="img" aria-label="Portrait of Marisa A. Hale"><div class="tag" style="top:160px">Marisa A. Hale</div></div>
    <div class="member" style="left:834px" role="img" aria-label="Portrait of Evander Pritchley"><div class="tag">Evander Pritchley, CPA, CA</div></div>
  </div>
</section>

<section class="payment">
  <div class="art" role="img" aria-label="Illustration of a 3D pie chart with a highlighted tax slice"></div>
  <h2>Payment</h2>
  <p>Lorem Ipsum is simply dummy text of the printing and typesetting industry. Lorem Ipsum has been the industry's standard dummy text ever since the 1500s, when an unknown printer took a galley of type and scrambled it to make a type specimen book.</p>
  <div class="actions"><span class="btn btn-blue">Read More</span><span class="btn btn-outline">Payment Form</span></div>
</section>

<section class="services">
  <div class="service ind">
    <div class="icon"><svg width="60" height="56" viewBox="0 0 60 56"><circle cx="22" cy="16" r="11" fill="#fff"/><path d="M2 54 Q22 20 42 54Z" fill="#fff"/><circle cx="42" cy="20" r="8" fill="var(--navy)"/></svg></div>
    <h3>For Individuals</h3>
    <p class="intro">We also provide advice and compliance services for individuals and/or businesses with Canadian tax issues and obligations:</p>
    <ul><li>Canadian personal tax returns</li><li>Advice</li><li>Residency consultations</li><li>Tax or estate planning</li><li>Cross-border business structuring</li></ul>
  </div>
  <div class="divider"></div>
  <div class="service firms">
    <div class="icon"><svg width="66" height="60" viewBox="0 0 66 60"><circle cx="33" cy="16" r="12" fill="#fff"/><text x="33" y="22" text-anchor="middle" font-size="16" font-weight="700" fill="var(--blue)" font-family="Arial">$</text><circle cx="12" cy="44" r="6" fill="#fff"/><circle cx="33" cy="44" r="6" fill="#fff"/><circle cx="54" cy="44" r="6" fill="#fff"/></svg></div>
    <h3>For Public Accounting Firms</h3>
    <p class="intro">Our core business is providing tax support for public accounting firms (PAFs).Working with Brindlemoor Tax Advisory offers PAFs the following benefits:</p>
    <ul><li>Risk mitigation</li><li>Cost reduction</li><li>Non-competition</li><li>Hourly rate alignment</li></ul>
  </div>
</section>

<section class="testimonial" role="img" aria-label="Blue-tinted office meeting room with a man by the window">
  <h2 class="section-title">What Our Client Say</h2>
  <blockquote>
    <svg class="quote-mark" width="40" height="32" viewBox="0 0 40 32"><path d="M2 30 V16 Q2 4 14 2 V8 Q8 10 8 16 H16 V30Z M22 30 V16 Q22 4 34 2 V8 Q28 10 28 16 H36 V30Z" fill="#fff"/></svg>
    Lorem Ipsum is simply dummy text of the printing and typesetting industry. Lorem Ipsum has been the industry's standard dummy text ever since the 1500s, when an unknown printer took a galley of type and scrambled it to make a type specimen book.
    <cite>- Tobias Wrenfield</cite>
    <span class="role">CEO, Lantern Co.</span>
  </blockquote>
  <div class="dots"><i class="on"></i><i></i><i></i></div>
</section>

<section class="blog">
  <h2 class="section-title">Latest Blog</h2>
  <div class="posts">
    <article class="post"><h4>Lorem Ipsum is simply dummy</h4><div class="date"><svg width="14" height="14" viewBox="0 0 14 14"><rect x="1" y="2" width="12" height="11" fill="none" stroke="var(--navy)" stroke-width="1.5"/><line x1="1" y1="5" x2="13" y2="5" stroke="var(--navy)" stroke-width="1.5"/></svg>Posted at 1-9-2017</div><p>No person involved in the authorization process may receive compensation for denial of care.</p></article>
    <article class="post"><h4>Lorem Ipsum is simply dummy</h4><div class="date"><svg width="14" height="14" viewBox="0 0 14 14"><rect x="1" y="2" width="12" height="11" fill="none" stroke="var(--navy)" stroke-width="1.5"/><line x1="1" y1="5" x2="13" y2="5" stroke="var(--navy)" stroke-width="1.5"/></svg>Posted at 2-9-2017</div><p>No person involved in the authorization process may receive compensation for denial of care.</p></article>
    <article class="post"><h4>Lorem Ipsum is simply dummy</h4><div class="date"><svg width="14" height="14" viewBox="0 0 14 14"><rect x="1" y="2" width="12" height="11" fill="none" stroke="var(--navy)" stroke-width="1.5"/><line x1="1" y1="5" x2="13" y2="5" stroke="var(--navy)" stroke-width="1.5"/></svg>Posted at 3-9-2017</div><p>No person involved in the authorization process may receive compensation for denial of care.</p></article>
  </div>
</section>

<div class="cta">
  <h2>Brindlemoor Tax Advisory</h2>
  <p>Corwin is chartered professional accountant (CPA) and an enrolled agent (EA).</p>
  <span class="btn btn-blue">Contact Us Now</span>
</div>

<footer class="site-footer">
  <div class="foot-col foot-brand">
    <div class="brand-square"></div>
    <div class="brand-name">Brindlemoor Tax Advisory</div>
    <p>Lorem Ipsum is simply dummy text of the printing and typesetting industry.</p>
    <div class="foot-social"><span></span><span></span><span></span><span></span></div>
  </div>
  <div class="foot-col foot-links">
    <h5>Usefull Links</h5>
    <ul><li>Home</li><li>Our Team</li><li>For Individuals</li><li>For Public Accounting Firms</li><li>Payment</li><li>Contact</li></ul>
  </div>
  <div class="foot-col foot-contact">
    <h5>Get In Touch</h5>
    <div class="row"><svg width="20" height="20" viewBox="0 0 20 20"><path d="M10 1 C5 1 3 5 3 8 C3 13 10 19 10 19 C10 19 17 13 17 8 C17 5 15 1 10 1Z" fill="none" stroke="var(--orange)" stroke-width="1.8"/><circle cx="10" cy="8" r="2.5" fill="var(--orange)"/></svg><span>418 Quarrystone Road, Unit 12<br>Eastport, Nova Scotia B0X 2Z0</span></div>
    <div class="row"><svg width="20" height="20" viewBox="0 0 20 20"><path d="M4 2 L8 2 L9 6 L7 8 Q9 12 12 13 L14 11 L18 12 L18 16 Q18 18 16 18 Q3 17 2 4 Q2 2 4 2Z" fill="var(--orange)"/></svg><span>(555) 014-2278</span></div>
    <div class="row"><svg width="20" height="20" viewBox="0 0 20 20"><rect x="5" y="2" width="10" height="5" fill="none" stroke="var(--orange)" stroke-width="1.6"/><rect x="2" y="7" width="16" height="7" fill="var(--orange)"/><rect x="5" y="12" width="10" height="6" fill="#fff" stroke="var(--orange)" stroke-width="1.6"/></svg><span>(555) 014-2278</span></div>
    <div class="row"><svg width="20" height="20" viewBox="0 0 20 20"><rect x="2" y="4" width="16" height="12" fill="none" stroke="var(--orange)" stroke-width="1.6"/><path d="M2 4 L10 11 L18 4" fill="none" stroke="var(--orange)" stroke-width="1.6"/></svg><span>help@brindlemoor.example</span></div>
  </div>
  <div class="foot-col foot-news">
    <h5>Newsletter</h5>
    <p class="hint">Subscribe to LedgerNote</p>
    <div class="field">Enter Email*</div>
    <span class="subscribe">Subscribe</span>
  </div>
  <div class="copyright">Copyright © 2017 Brindlemoor Tax Advisory Inc.</div>
</footer>

</body>
</html>
```